Business Card Design

Very plain simple card, Plain modern font. Background. Grey fading to black. Large Bright lime green text. Saying.

GLR-VU.COM

Small other details in white text.

Irish Horse Sales . Livery . Stud . Shows

Mark Dwyerson
GLR
Ashby Croft
Wolverdale Lane
Carbeckthorpe
Lincolnshire
LN7 2WT

Email. Glrvus@mailnest.co.uk
Tel. 07482 604319

Business

As below

```html
<!DOCTYPE html>
<html lang="en">
<head>
<meta charset="utf-8">
<title>GLR-VU.COM Business Card</title>
<link rel="stylesheet" href="https://fonts.googleapis.com/css2?family=Quicksand:wght@400;500&display=swap">
<style>
  :root {
    --page-bg: #d9d9d9;
    --card-center: #4b4b4d;
    --card-mid: #1e1e20;
    --card-edge: #0b0b0c;
    --lime: #6fcf3b;
    --white: #f2f2f2;
  }
  * { margin: 0; padding: 0; box-sizing: border-box; }
  html, body {
    width: 1200px;
    height: 800px;
    overflow: hidden;
  }
  body {
    background: var(--page-bg);
    display: flex;
    align-items: center;
    justify-content: center;
    font-family: "Quicksand", sans-serif;
  }
  .business-card {
    width: 980px;
    height: 560px;
    background: radial-gradient(ellipse 75% 80% at 50% 38%, var(--card-center) 0%, var(--card-mid) 55%, var(--card-edge) 100%);
    display: flex;
    flex-direction: column;
    align-items: center;
    justify-content: center;
    text-align: center;
  }
  .brand-name {
    font-family: "Quicksand", sans-serif;
    font-weight: 500;
    font-size: 92px;
    line-height: 1;
    color: var(--lime);
  }
  .brand-services {
    margin-top: 18px;
    font-family: "Quicksand", sans-serif;
    font-weight: 500;
    font-size: 24px;
    letter-spacing: 1px;
    color: var(--white);
    text-transform: uppercase;
    white-space: nowrap;
  }
  .contact-block {
    margin-top: 44px;
    color: var(--white);
  }
  .contact-name {
    font-size: 30px;
    font-weight: 400;
    color: var(--lime);
    text-transform: uppercase;
    letter-spacing: 1px;
    line-height: 1.1;
  }
  .contact-company {
    font-size: 21px;
    margin-bottom: 16px;
  }
  .contact-address {
    font-style: normal;
    font-size: 23px;
    line-height: 1.3;
  }
  .contact-lines {
    margin-top: 4px;
    font-size: 23px;
  }
  .contact-label { color: var(--lime); }
  .contact-gap { display: inline-block; width: 26px; }
</style>
</head>
<body>
  <article class="business-card">
    <header class="brand-block">
      <h1 class="brand-name">GLR-VU.COM</h1>
      <p class="brand-services">Irish Horse Sales . Livery . Stud . Shows</p>
    </header>
    <section class="contact-block">
      <p class="contact-name">Mark Dwyerson</p>
      <p class="contact-company">GLR</p>
      <address class="contact-address">
        Ashby Croft, Wolverdale Lane<br>
        Carbeckthorpe, Lincolnshire, LN7 2WT
      </address>
      <p class="contact-lines">
        <span class="contact-label">Email</span> Glrvus@mailnest.co.uk<span class="contact-gap"></span><span class="contact-label">Tel.</span> 07482 604319
      </p>
    </section>
  </article>
</body>
</html>
```